Website redesign for job agency recruitment

Please refer to the attached document, “Harbor Work Portal Outline,” for comprehensive details regarding the scope, objectives, and requirements of this website redesign project.

For imagery you can use images from this website https://www.pixvaultmedia.com or any other you regularly use.

Target Market(s)

Jobseekers and Companies looking for general labour

Industry/Entity Type

Services: Oil, Gas and Mining, Administrative, Construction and Trades, Warehouse and Logistics and, Manufacturing.

Number of Pages Required

5+ page

Font styles to use
Serif
Other font styles liked:
• Inter, Open-Sans or similar.

Requirements
Must have
• The requirements highlighted in the Word document attached. The final design needs to be provided in Figma including all viewports (Desktop, mobiel and tablet)
Should not have
• Website we like as a reference: www.beltonworkforceinc.com, www.veltaworkforce.com, www.zplacer.com, www.brimwellworkforce.com, www.9tworkcrew.com, www.hiringonthemove.ca

```html
<!DOCTYPE html>
<html lang="en">
<head>
<meta charset="utf-8">
<title>Harbor Work Agency</title>
<link rel="stylesheet" href="https://fonts.googleapis.com/css2?family=Inter:wght@400;500;600;700;800;900&display=swap">
<style>
:root{
  --navy:#0b3a8f;
  --blue:#0d47a8;
  --band-a:#0a2f82;
  --band-b:#0b3fa3;
  --yellow:#f6c515;
  --ink:#1b1b1b;
  --muted:#555;
  --line:#d8dbe2;
  --white:#fff;
}
*{box-sizing:border-box;margin:0;padding:0}
html,body{width:1200px;height:3741px;overflow:hidden}
body{position:relative;font-family:"Inter",sans-serif;color:var(--ink);background:var(--white)}
.abs{position:absolute}
.btn{position:absolute;display:flex;align-items:center;justify-content:center;font-weight:700;font-size:12px;border-radius:5px;background:var(--blue);color:var(--white)}
.btn-light{background:var(--white);color:var(--blue)}
.section-title{position:absolute;left:0;width:1200px;text-align:center;font-weight:800;font-size:32px;color:var(--navy);letter-spacing:.2px}
.section-title span{position:relative;display:inline-block}
.section-title span::after{content:"";position:absolute;left:50%;bottom:-6px;width:70px;margin-left:-35px;height:2px;background:var(--yellow)}
/* header */
.site-header{position:absolute;top:0;left:0;width:1200px;height:64px;background:var(--white)}
.brand-card{position:absolute;left:157px;top:0;width:138px;height:112px;background:var(--white);border-radius:0 0 10px 10px;box-shadow:0 4px 12px rgba(0,0,0,.12);z-index:3;display:flex;flex-direction:column;align-items:center;justify-content:center;text-align:center}
.brand-name{font-weight:800;font-size:28px;color:var(--navy);line-height:1}
.brand-full{font-size:9px;font-weight:600;color:var(--navy);margin-top:8px}
.brand-tag{font-size:5.5px;color:#777;margin-top:2px}
.nav a{position:absolute;top:25px;font-size:12px;font-weight:500;color:var(--navy);text-decoration:none}
.nav a.active{color:var(--yellow);border-bottom:1px solid var(--yellow);padding-bottom:1px}
/* hero */
.hero-photo{position:absolute;top:64px;left:0;width:1200px;height:620px;background:linear-gradient(180deg,#3a2c22 0%,#6b4a30 45%,#2a2220 100%)}
.hero-title{position:absolute;top:240px;left:0;width:1200px;text-align:center;font-weight:900;font-size:54px;line-height:54px;color:var(--yellow);letter-spacing:-.5px}
.hero-btn{height:40px;border-radius:20px;border:2px solid #9fb4e8;font-size:14px}
/* services */
.service-item{position:absolute;font-size:15px;font-weight:600;color:var(--ink);display:flex;align-items:center;gap:10px}
.service-item i{display:block;width:22px;height:22px;border-radius:50%;background:var(--blue)}
.service-item.active{color:var(--yellow)}
.service-item.active i{background:var(--yellow)}
.photo{position:absolute;border-radius:10px}
.service-copy h3{font-size:15px;font-weight:700;color:var(--navy)}
.service-copy p{font-size:10px;line-height:12px;color:var(--ink);margin-top:6px;width:200px}
/* about */
.about-band{position:absolute;top:1260px;left:0;width:1200px;height:552px;background:linear-gradient(180deg,var(--band-a),var(--band-b))}
.exp-box{position:absolute;left:418px;top:1540px;width:163px;height:148px;background:var(--yellow);border:6px solid var(--band-a);border-radius:10px;padding:28px 16px;color:var(--navy)}
.exp-box b{display:block;font-size:34px;font-weight:900;line-height:34px}
.exp-box span{display:block;font-size:17px;font-weight:800;line-height:21px;margin-top:6px}
.about-copy{position:absolute;left:644px;top:1378px;width:385px;color:var(--white)}
.about-copy h2{font-size:32px;font-weight:800;display:inline-block;border-bottom:2px solid var(--yellow);padding-bottom:2px}
.about-copy h4{font-size:12px;font-weight:700;line-height:15px;margin-top:20px}
.about-copy p{font-size:10.5px;line-height:13px;margin-top:14px}
/* testimonials */
.t-card{position:absolute;top:1961px;width:276px;height:215px;background:var(--white);border-radius:6px;box-shadow:0 2px 14px rgba(0,0,0,.08);padding:22px 18px}
.avatar{width:36px;height:36px;border-radius:50%;background:linear-gradient(135deg,#c9b8a8,#7a6a5e)}
.stars{color:var(--yellow);font-size:13px;letter-spacing:3px;margin-top:8px}
.t-card p{font-size:10.5px;line-height:16px;color:#333;margin-top:8px}
.t-card h5{font-size:10px;font-weight:700;color:var(--blue);margin-top:10px}
.t-card small{font-size:8px;color:#aaa}
.arrow{position:absolute;top:2215px;width:16px;height:16px}
/* blog */
.blog-band{position:absolute;top:2326px;left:0;width:1200px;height:530px;background:linear-gradient(180deg,var(--band-b),var(--band-a))}
.blog-title{color:var(--yellow)}
.blog-img{position:absolute;top:2464px;width:277px;height:186px}
.blog-meta{position:absolute;top:2666px;display:flex;align-items:center;gap:8px;font-size:10px;color:var(--white)}
.blog-meta i{display:block;width:20px;height:20px;border-radius:50%;background:var(--yellow)}
.blog-text{position:absolute;top:2696px;width:260px;font-size:11.5px;line-height:16px;color:var(--white)}
/* inquiry */
.field{position:absolute;border:1px solid var(--line);font-size:10px;color:#999;padding:10px 12px}
/* footer */
.f-title{position:absolute;font-size:12px;font-weight:700;color:var(--yellow)}
.f-list{position:absolute;list-style:none;font-size:10.5px;color:var(--white);line-height:19.4px}
.f-list li.active{color:var(--yellow);text-decoration:underline}
.f-contact{position:absolute;display:flex;gap:8px;color:var(--white);font-size:11.5px;line-height:14px;font-weight:600}
.f-contact em{font-style:normal;color:#5f95ff;font-weight:500;display:block}
.f-contact i{flex:none;width:28px;height:28px;border-radius:50%;border:1.5px solid var(--yellow);background:var(--blue);display:flex;align-items:center;justify-content:center}
.social{position:absolute;top:3615px;width:25px;height:25px;border-radius:50%;background:var(--blue);border:1.5px solid var(--white)}
.bottom-bar{position:absolute;top:3708px;left:0;width:1200px;height:33px;background:var(--blue);font-size:11px;color:var(--white)}
</style>
</head>
<body>

<!-- header -->
<header class="site-header">
  <div class="brand-card">
    <div class="brand-name">HWA</div>
    <div class="brand-full">Harbor Work Agency Ltd.</div>
    <div class="brand-tag">The right team for your growing business</div>
  </div>
  <nav class="nav">
    <a class="active" style="left:493px">Home</a>
    <a style="left:548px">Candidates</a>
    <a style="left:633px">Employers</a>
    <a style="left:713px">About Us</a>
    <a style="left:788px">Contact Us</a>
  </nav>
  <div class="btn" style="left:905px;top:17px;width:138px;height:31px">Client Registration</div>
</header>

<!-- hero -->
<div class="hero-photo" role="img" aria-label="City skyline of tall towers at sunset"></div>
<svg class="abs" style="top:0;left:0" width="1200" height="700" viewBox="0 0 1200 700" aria-hidden="true">
  <path d="M0,470 C250,600 700,660 1200,520 L1200,700 L0,700 Z" fill="#fff"/>
  <path d="M0,430 C150,520 350,585 660,600 C400,612 150,565 0,505 Z" fill="#f6c515"/>
  <path d="M0,525 C150,585 300,603 520,608 C300,616 120,595 0,565 Z" fill="#f6c515"/>
  <path d="M130,598 C450,625 900,560 1200,438 L1200,520 C900,650 450,690 140,606 Z" fill="#0d47a8"/>
</svg>
<h1 class="hero-title">OUR GOAL IS<br>YOUR SUCCESS</h1>
<div class="btn hero-btn" style="left:445px;top:375px;width:151px">For Candidates</div>
<div class="btn hero-btn" style="left:610px;top:375px;width:144px">For Employers</div>

<!-- services -->
<h2 class="section-title" style="top:752px"><span>OUR SERVICES</span></h2>
<svg class="abs" style="top:800px;left:160px" width="120" height="370" aria-hidden="true">
  <path d="M15,5 C90,120 95,250 15,365" fill="none" stroke="#cfcfcf" stroke-width="1.2"/>
</svg>
<div class="service-item active" style="left:204px;top:850px"><i></i>Oil, Gas &amp; Mining</div>
<div class="service-item" style="left:226px;top:910px"><i></i>Administrative</div>
<div class="service-item" style="left:232px;top:971px"><i></i>Construction &amp; Trades</div>
<div class="service-item" style="left:226px;top:1031px"><i></i>Warehouse &amp; Logistics</div>
<div class="service-item" style="left:204px;top:1090px"><i></i>Manufacturing</div>
<div class="photo" style="left:474px;top:824px;width:306px;height:302px;background:linear-gradient(135deg,#5c6f86,#c98a4a 60%,#e86a28)" role="img" aria-label="Worker in hard hat at an oil refinery"></div>
<div class="service-copy abs" style="left:837px;top:836px">
  <h3>Oil, Gas &amp; Mining</h3>
  <p>Harbor Work Agency Is A Premiere Oil, Gas &amp; Mining Staffing Agency That Can Provide You With A Reliable And Experienced Workforce. From Rig Hands To Engineers, We Provide Solutions From Temp, Temp-To-Hire, And Permanent Positions.</p>
</div>
<div class="btn" style="left:837px;top:957px;width:76px;height:25px;font-size:10px;border-radius:3px">Read More</div>
<div class="abs" style="left:840px;top:1046px;font-size:40px;font-weight:800;color:var(--navy)">HWA</div>

<!-- about -->
<section class="about-band"></section>
<div class="photo" style="left:142px;top:1335px;width:388px;height:401px;border-radius:6px;background:linear-gradient(135deg,#e9ecef,#9aa4b3 60%,#4a5568)" role="img" aria-label="Smiling businessman in a suit holding documents"></div>
<div class="exp-box"><b>20+</b><span>YEAR OF<br>EXPERIENCE</span></div>
<div class="about-copy">
  <h2>ABOUT US</h2>
  <h4>Harbor Work Agency Offers A Complete Range Of Staffing Services To Keep Pace With Your Career Or Operational Demands.</h4>
  <p>We Understand It's Not Only Daunting But Very Costly In Both Time And Money To Make Your Business Thrive In A Rapidly Changing Environment.</p>
  <p>Our Staffing And Recruitment Services Are Not Just Limited To Finding Good People. We Are A Canada-Wide Team Of Capable Search Specialists, Career Counselors, HR Specialists, And Business Consultants Who Enjoy Providing Our Clients With A Very Customized Staffing Solution That Evolves Within Their Market. Each Project Provides A Chance For Us To Apply Our Knowledge And Shine.</p>
</div>
<div class="btn btn-light" style="left:644px;top:1655px;width:95px;height:30px;border-radius:4px">Read More</div>

<!-- testimonials -->
<h2 class="section-title" style="top:1892px"><span>TESTIMONIALS</span></h2>
<div class="t-card" style="left:168px">
  <div class="avatar" role="img" aria-label="Client portrait"></div>
  <div class="stars">★★★★★</div>
  <p>Lorem Ipsum Is Simply Dummy Text Of The Printing And Typesetting Industry. Lorem Ipsum Has Been The Industry's Standard Dummy Text Ever Since The 1500s...</p>
  <h5>Dana Whitlow</h5><small>Feb 10, 2026</small>
</div>
<div class="t-card" style="left:462px">
  <div class="avatar" role="img" aria-label="Client portrait"></div>
  <div class="stars">★★★★★</div>
  <p>Lorem Ipsum Is Simply Dummy Text Of The Printing And Typesetting Industry. Lorem Ipsum Has Been The Industry's Standard Dummy Text Ever Since The 1500s...</p>
  <h5>Owen Barrick</h5><small>Jan 15, 2026</small>
</div>
<div class="t-card" style="left:755px">
  <div class="avatar" role="img" aria-label="Client portrait"></div>
  <div class="stars">★★★★★</div>
  <p>Lorem Ipsum Is Simply Dummy Text Of The Printing And Typesetting Industry. Lorem Ipsum Has Been The Industry's Standard Dummy Text Ever Since The 1500s...</p>
  <h5>Owen Barrick</h5><small>Jan 20, 2026</small>
</div>
<svg class="arrow" style="left:527px" viewBox="0 0 16 16" aria-hidden="true"><path d="M13 8H3M7 4L3 8l4 4" fill="none" stroke="#222" stroke-width="1.5"/></svg>
<div class="btn" style="left:552px;top:2208px;width:83px;height:30px">View All</div>
<svg class="arrow" style="left:645px" viewBox="0 0 16 16" aria-hidden="true"><path d="M3 8h10M9 4l4 4-4 4" fill="none" stroke="#222" stroke-width="1.5"/></svg>

<!-- blog -->
<section class="blog-band"></section>
<h2 class="section-title blog-title" style="top:2394px"><span>OUR BLOG</span></h2>
<div class="blog-img" style="left:157px;background:linear-gradient(135deg,#dfe3e6,#8a96a3)" role="img" aria-label="Colleagues working at a laptop in an office"></div>
<div class="blog-img" style="left:461px;background:linear-gradient(180deg,#3b4a66,#e8a24a 55%,#7a4a2a)" role="img" aria-label="Rooftop terrace at sunrise over the city"></div>
<div class="blog-img" style="left:766px;background:linear-gradient(135deg,#2c3a2e,#8f9a78 60%,#e7e2c9)" role="img" aria-label="Downtown street with sunlight between buildings"></div>
<div class="blog-meta" style="left:169px"><i></i>Feb 10, 2026</div>
<div class="blog-meta" style="left:473px"><i></i>Jan 15, 2026</div>
<div class="blog-meta" style="left:777px"><i></i>Jan 15, 2026</div>
<div class="blog-text" style="left:169px">Lorem Ipsum Is Simply Dummy Text Of The Printing And Typesetting Industry...</div>
<div class="blog-text" style="left:473px">Lorem Ipsum Is Simply Dummy Text Of The Printing And Typesetting Industry...</div>
<div class="blog-text" style="left:777px">Lorem Ipsum Is Simply Dummy Text Of The Printing And Typesetting Industry...</div>
<div class="btn btn-light" style="left:559px;top:2750px;width:82px;height:31px">View All</div>

<!-- inquiry -->
<h2 class="section-title" style="top:2923px"><span>QUICK INQUIRY</span></h2>
<div class="field" style="left:356px;top:2993px;width:237px;height:33px">First Name</div>
<div class="field" style="left:606px;top:2993px;width:237px;height:33px">Last Name</div>
<div class="field" style="left:356px;top:3042px;width:237px;height:33px">Email</div>
<div class="field" style="left:606px;top:3042px;width:237px;height:33px">Phone</div>
<div class="field" style="left:356px;top:3092px;width:487px;height:79px">How Can We Help?</div>
<div class="btn" style="left:561px;top:3203px;width:77px;height:31px">Submit</div>

<!-- footer -->
<svg class="abs" style="top:3330px;left:0" width="1200" height="380" viewBox="0 0 1200 380" aria-hidden="true">
  <defs><linearGradient id="footerShade" x1="0" y1="0" x2="0" y2="1"><stop offset="0" stop-color="#3a2a1e"/><stop offset="1" stop-color="#161414"/></linearGradient></defs>
  <path d="M0,175 C300,65 700,25 1200,95 L1200,380 L0,380 Z" fill="url(#footerShade)" role="img" aria-label="Dark city skyline at dusk"/>
  <path d="M0,115 C300,25 700,-5 1080,60 C700,40 300,85 0,205 Z" fill="#0d47a8"/>
  <path d="M640,30 C900,35 1100,75 1200,100 L1200,145 C1050,100 900,65 640,30 Z" fill="#f6c515"/>
  <path d="M780,75 C950,90 1100,125 1200,165 L1200,185 C1080,140 950,105 780,75 Z" fill="#f6c515"/>
</svg>
<div class="abs" style="left:157px;top:3477px;width:155px;height:133px;background:#fff;border-radius:8px;display:flex;flex-direction:column;align-items:center;justify-content:center">
  <div class="brand-name" style="font-size:34px">HWA</div>
  <div class="brand-full">Harbor Work Agency Ltd.</div>
  <div class="brand-tag">The right team for your growing business</div>
</div>

<div class="f-title" style="left:382px;top:3476px">CONTACT INFO</div>
<div class="f-contact" style="left:382px;top:3508px">
  <i><svg width="12" height="12" viewBox="0 0 24 24"><path d="M6.6 10.8a15 15 0 006.6 6.6l2.2-2.2c.3-.3.7-.4 1-.2 1.1.4 2.3.6 3.6.6.6 0 1 .4 1 1V20c0 .6-.4 1-1 1A17 17 0 013 4c0-.6.4-1 1-1h3.5c.6 0 1 .4 1 1 0 1.3.2 2.5.6 3.6.1.3 0 .7-.2 1z" fill="#fff"/></svg></i>
  <div><em>British Columbia</em>555-310-4471</div>
</div>
<div class="f-contact" style="left:533px;top:3508px">
  <i><svg width="12" height="12" viewBox="0 0 24 24"><path d="M6.6 10.8a15 15 0 006.6 6.6l2.2-2.2c.3-.3.7-.4 1-.2 1.1.4 2.3.6 3.6.6.6 0 1 .4 1 1V20c0 .6-.4 1-1 1A17 17 0 013 4c0-.6.4-1 1-1h3.5c.6 0 1 .4 1 1 0 1.3.2 2.5.6 3.6.1.3 0 .7-.2 1z" fill="#fff"/></svg></i>
  <div><em>Alberta</em>555-228-6190</div>
</div>
<div class="f-contact" style="left:382px;top:3558px">
  <i><svg width="12" height="12" viewBox="0 0 24 24"><rect x="3" y="5" width="18" height="14" rx="2" fill="#fff"/><path d="M3 6l9 7 9-7" fill="none" stroke="#0d47a8" stroke-width="2"/></svg></i>
  <div><em>Email</em>info@harborworkagency.ca</div>
</div>
<div class="f-contact" style="left:382px;top:3608px">
  <i><svg width="12" height="12" viewBox="0 0 24 24"><circle cx="12" cy="12" r="9" fill="none" stroke="#fff" stroke-width="2"/><path d="M12 7v5l3 2" fill="none" stroke="#fff" stroke-width="2"/></svg></i>
  <div><em style="display:inline">Mon - Fri:</em> 8am - 5pm<br><em style="display:inline">Sat-Sun:</em> Close</div>
</div>

<div class="f-title" style="left:710px;top:3476px">QUICK LINKS</div>
<ul class="f-list" style="left:710px;top:3494px">
  <li class="active">Home</li><li>Candidates</li><li>Employers</li><li>Terms Of Use</li><li>About Us</li><li>Contact Us</li><li>Vancouver Location</li><li>Client Registration</li>
</ul>
<div class="f-title" style="left:883px;top:3476px">OUR LOCATIONS</div>
<ul class="f-list" style="left:883px;top:3494px">
  <li>Calgary</li><li>Toronto</li><li>Vancouver</li>
</ul>
<div class="f-title" style="left:883px;top:3588px">SOCIAL MEDIA</div>
<div class="social" style="left:883px"></div>
<div class="social" style="left:915px;background:var(--yellow)"></div>
<div class="social" style="left:947px"></div>
<div class="social" style="left:981px"></div>

<div class="bottom-bar">
  <span class="abs" style="left:157px;top:10px">© 2026 Harbor Work. All Right Reserved</span>
  <span class="abs" style="left:929px;top:10px;color:#8fa8de">Terms Of Use</span>
  <span class="abs" style="left:1016px;top:10px;color:#8fa8de">Login</span>
</div>

</body>
</html>
```